Poster of Insipirational Quotes

Attached is a list of leadership quotes from Arlen Drubeck. I would like a poster made, incorporating whatever design elements you like, potentially including Arlen's face, and one or more of the quotes. I intend to print this out in A3 or larger to hang on my wall.

The quotes are:

Being responsible sometimes means pissing people off.

The day soldiers stop bringing you their problems is the day you have stopped leading them.

Don't be buffaloed by experts and elites. Experts often possess more data than judgment. Elites can become so inbred that they produce hemophiliacs who bleed to death as soon as they are nicked by the real world.

Don't be afraid to challenge the pros, even in their own backyard.

Never neglect details. When everyone's mind is dulled or distracted the leader must be doubly vigilant.

You don't know what you can get away with until you try.

Keep looking below surface appearances. Don't shrink from doing so (just) because you might not like what you find.

Organization doesn't really accomplish anything. Plans don't accomplish anything, either. Theories of management don't much matter. Endeavors succeed or fail because of the people involved. Only by attracting the best people will you accomplish great deeds.

Organization charts and fancy titles count for next to nothing.

Never let your ego get so close to your position that when your position goes, your ego goes with it.

Fit no stereotypes. Don't chase the latest management fads. The situation dictates which approach best accomplishes the team's mission.

Perpetual optimism is a force multiplier.

Look for intelligence and judgment, and most critically, a capacity to anticipate, to see around corners. Also look for loyalty, integrity, a high energy drive, a balanced ego, and the drive to get things done.

Great leaders are almost always great simplifiers, who can cut through argument, debate and doubt, to offer a solution everybody can understand.

The commander in the field is always right and the rear echelon is wrong, unless proved otherwise.

Have fun in your command. Don't always run at a breakneck pace. Take leave when you've earned it: Spend time with your families. Corollary: surround yourself with people who take their work seriously, but not themselves, those who work hard and play hard.

Command is lonely.

Leadership is the art of accomplishing more than the science of management
says is possible.
Updates

I need to modify the specification based on the designs that I've seen.

Target Market(s)

Executive Office

Colors

Designer to choose colors to be used in the design.

Requirements
Must have
• Quotes

```html
<!DOCTYPE html>
<html lang="en">
<head>
<meta charset="utf-8">
<title>Arlen Drubeck – Leadership Quote Posters</title>
<link rel="stylesheet" href="https://fonts.googleapis.com/css2?family=Stardos+Stencil:wght@700&family=Germania+One&family=Old+Standard+TT:wght@700&family=Anton&display=swap">
<style>
  :root {
    --paper: #ffffff;
    --frame-red: #e8333c;
    --frame-red-deep: #e21f26;
    --frame-navy: #343a78;
    --frame-black: #231f20;
    --ink: #111111;
    --navy-ink: #2c3577;
    --blood: #c4161c;
    --ornament: #a11d21;
    --photo-light: #c9c9c9;
    --photo-mid: #8f8f8f;
    --panel-light: #eef0f2;
    --dark-1: #121212;
    --dark-2: #3b3b3b;
  }
  html, body {
    margin: 0;
    padding: 0;
    overflow: hidden;
    background: var(--paper);
  }
  .canvas {
    position: relative;
    width: 905px;
    height: 1200px;
    overflow: hidden;
    background: var(--paper);
  }
  .poster, .frame, .portrait, .quote, .title-box, .flourish { position: absolute; box-sizing: border-box; }

  /* Poster 1 – optimism */
  .poster--optimism { left: 10px; top: 16px; width: 430px; height: 571px; border: 9px solid var(--frame-red); background: var(--paper); }
  .poster--optimism .frame { left: 12px; top: 15px; width: 390px; height: 522px; border: 9px solid var(--frame-navy); background: var(--paper); }
  .poster--optimism .portrait { left: 2px; top: 50px; width: 355px; height: 446px;
    background: linear-gradient(180deg, var(--photo-light) 0%, var(--photo-mid) 100%);
    clip-path: polygon(28% 0, 62% 0, 70% 45%, 100% 58%, 100% 100%, 0 100%, 0 58%, 22% 45%); }
  .poster--optimism .quote { left: 258px; top: 288px; width: 110px; text-align: center;
    font-family: "Stardos Stencil", "Impact", sans-serif; font-weight: 700; font-size: 13px; line-height: 19px; color: var(--ink); letter-spacing: 0.5px; }
  .poster--optimism .quote .emph { font-size: 17px; }

  /* Poster 2 – responsibility */
  .poster--responsible { left: 464px; top: 15px; width: 430px; height: 572px; border: 11px solid var(--frame-red-deep); background: var(--paper); }
  .poster--responsible .frame { left: 9px; top: 14px; width: 392px; height: 522px; border: 9px solid var(--frame-black); background: var(--paper); }
  .poster--responsible .portrait { left: 77px; top: 50px; width: 240px; height: 314px; border-radius: 46% 46% 44% 44% / 40% 40% 58% 58%;
    background: linear-gradient(180deg, var(--photo-mid) 0%, var(--photo-light) 100%); }
  .poster--responsible .quote { left: 0; width: 374px; top: 378px; text-align: center; color: var(--ink);
    font-family: "Stardos Stencil", "Impact", sans-serif; font-weight: 700; }
  .poster--responsible .quote span { display: block; }
  .poster--responsible .line-a { font-size: 21px; line-height: 30px; }
  .poster--responsible .line-b { font-size: 14px; line-height: 32px; }
  .poster--responsible .line-c { font-size: 21px; line-height: 36px; }

  /* Poster 3 – experts */
  .poster--experts { left: 0; top: 604px; width: 449px; height: 596px;
    background: linear-gradient(90deg, var(--dark-1) 0%, var(--dark-2) 50%, var(--dark-1) 100%); }
  .poster--experts .frame { left: 31px; top: 42px; width: 385px; height: 514px;
    background: linear-gradient(180deg, var(--paper) 0%, var(--panel-light) 100%); }
  .poster--experts .flourish { left: 120px; width: 150px; height: 22px; }
  .poster--experts .flourish--top { top: 0; background: linear-gradient(90deg, transparent, var(--ornament) 30%, var(--ornament) 70%, transparent); opacity: .55; height: 3px; top: 14px; }
  .poster--experts .flourish--bottom { top: 97px; background: linear-gradient(90deg, transparent, var(--ornament) 30%, var(--ornament) 70%, transparent); opacity: .55; height: 3px; }
  .poster--experts .title-box { left: 58px; top: 48px; width: 272px; height: 52px; }
  .poster--experts .title-text { position: absolute; inset: 0; display: flex; align-items: center; justify-content: center;
    font-family: "Germania One", "Georgia", serif; font-size: 25px; letter-spacing: 3px; color: var(--ink); }
  .poster--experts .portrait { left: 10px; top: 110px; width: 305px; height: 404px;
    background: linear-gradient(180deg, var(--photo-light) 0%, var(--photo-mid) 100%);
    clip-path: polygon(30% 0, 65% 0, 72% 48%, 100% 60%, 100% 100%, 0 100%, 0 58%, 24% 48%); }
  .poster--experts .quote { left: 188px; top: 332px; width: 190px; text-align: center;
    font-family: "Old Standard TT", "Times New Roman", serif; font-weight: 700; font-size: 12px; line-height: 13.6px; color: var(--ink); }
  .poster--experts .quote .navy { color: var(--navy-ink); font-weight: 400; }
  .poster--experts .quote .red { color: var(--blood); font-weight: 400; }

  /* Poster 4 – try */
  .poster--try { left: 530px; top: 700px; width: 310px; height: 400px; }
  .poster--try .portrait { left: 8px; top: 5px; width: 256px; height: 387px; border-radius: 48% 20% 30% 55% / 35% 10% 30% 65%;
    background: linear-gradient(90deg, var(--photo-mid) 0%, var(--photo-light) 100%); }
  .poster--try .quote { left: 154px; top: 0; font-family: "Anton", "Impact", sans-serif; font-size: 40px; line-height: 41.5px;
    color: var(--ink); text-transform: uppercase; letter-spacing: -0.5px; }
  .poster--try .quote .ghost { color: var(--photo-mid); }
</style>
</head>
<body>
<main class="canvas">

  <section class="poster poster--optimism">
    <div class="frame">
      <div class="portrait" role="img" aria-label="Greyscale halftone portrait of Arlen Drubeck in suit and tie"></div>
      <p class="quote" style="margin:0">PERPETUAL<br><span class="emph">OPTIMISM</span><br>IS A<br>FORCE<br>MULTIPLIER.</p>
    </div>
  </section>

  <section class="poster poster--responsible">
    <div class="frame">
      <div class="portrait" role="img" aria-label="Greyscale halftone head portrait of Arlen Drubeck wearing glasses"></div>
      <p class="quote" style="margin:0">
        <span class="line-a">BEING RESPONSIBLE</span>
        <span class="line-b">SOMETIMES MEANS PISSING</span>
        <span class="line-c">PEOPLE OFF.</span>
      </p>
    </div>
  </section>

  <section class="poster poster--experts">
    <div class="frame">
      <div class="portrait" role="img" aria-label="Greyscale halftone portrait of Arlen Drubeck in suit and tie"></div>
      <p class="quote" style="margin:0">DON'T BE BUFFALOED BY<br><span class="navy">EXPERTS</span> AND <span class="navy">ELITES</span>.<br><span class="navy">EXPERTS</span> OFTEN POSSESS<br>MORE DATA THAN<br>JUDGMENT.<br><span class="navy">ELITES</span> CAN BECOME SO<br>INBRED THAT THEY<br>PRODUCE HEMOPHILIACS<br>WHO <span class="red">BLEED</span> TO DEATH AS<br>SOON AS THEY ARE<br>NICKED BY THE REAL<br>WORLD.</p>
    </div>
    <div class="flourish flourish--top" role="img" aria-label="Red scroll ornament above the title"></div>
    <svg class="title-box" viewBox="0 0 272 52" aria-hidden="true">
      <polygon points="14,2 258,2 270,26 258,50 14,50 2,26" fill="none" stroke="var(--navy-ink)" stroke-width="1.5"/>
    </svg>
    <div class="title-box"><span class="title-text">ARLEN DRUBECK</span></div>
    <div class="flourish flourish--bottom" role="img" aria-label="Red scroll ornament below the title"></div>
  </section>

  <section class="poster poster--try">
    <div class="portrait" role="img" aria-label="High-contrast greyscale portrait of Arlen Drubeck's face"></div>
    <p class="quote" style="margin:0">YOU<br>DON'T<br>KNOW<br>WHAT<br>YOU CAN<br>GET AWAY<br><span class="ghost">WITH</span><br><span class="ghost">UNTIL</span><br>YOU<br>TRY.</p>
  </section>

</main>
</body>
</html>
```